Tutorial design for a website

Design the tutorial as a PDF following the design of brindlequay.io
The website is already designed we need the tutorial to follow the llok and feel.

```html
<!DOCTYPE html>
<html lang="en">
<head>
<meta charset="utf-8">
<title>Brindlequay Copy Trading Tutorial – Step 3</title>
<link rel="stylesheet" href="https://fonts.googleapis.com/css2?family=Cinzel:wght@700;900&family=Lexend:wght@400;500;700&family=Inter:wght@400;500;600;700&display=swap">
<style>
  :root {
    --lime: #d7f36a;
    --ink: #1f1f1f;
    --paper: #ffffff;
    --screen: #1b1c20;
    --card: #25272d;
    --gold: #f0b90b;
    --white: #f5f5f5;
    --muted: #8a8d94;
    --down: #f0506e;
    --alert: #e8321f;
  }
  * { margin: 0; padding: 0; box-sizing: border-box; }
  html, body { width: 1200px; height: 800px; overflow: hidden; background: var(--paper); }
  .page { position: relative; width: 1200px; height: 800px; background: var(--paper); color: var(--ink); font-family: "Lexend", sans-serif; }
  .frame { position: absolute; left: 48px; top: 48px; width: 1104px; height: 722px; border: 2px solid var(--lime); }
  .step-title { position: absolute; left: 92px; top: 80px; font-family: "Cinzel", serif; font-weight: 900; font-size: 37px; letter-spacing: 1px; line-height: 1; }
  .section-tag { position: absolute; left: 50px; top: 135px; width: 357px; height: 50px; background: var(--lime); font-size: 19px; font-weight: 400; line-height: 50px; padding-left: 40px; letter-spacing: 0.4px; white-space: nowrap; }
  .section-tag strong { font-weight: 700; }
  .body-text { position: absolute; left: 90px; font-size: 19.5px; font-weight: 400; line-height: 29px; letter-spacing: 0.5px; color: #222; white-space: nowrap; }
  .t1 { top: 201px; }
  .t2 { top: 260px; }
  .t3 { top: 656px; }

  .screen { position: absolute; left: 88px; top: 351px; width: 1029px; height: 290px; background: var(--screen); font-family: "Inter", sans-serif; color: var(--white); overflow: hidden; }
  .nav { position: absolute; left: 0; top: 0; width: 100%; height: 44px; }
  .brand { position: absolute; left: 16px; top: 14px; display: flex; align-items: center; gap: 5px; color: var(--gold); font-weight: 700; font-size: 12.5px; letter-spacing: 0.5px; }
  .brand-mark { width: 11px; height: 11px; background: var(--gold); }
  .nav-links { position: absolute; left: 127px; top: 16px; display: flex; gap: 18px; font-size: 9.5px; font-weight: 500; }
  .deposit { position: absolute; left: 797px; top: 10px; width: 68px; height: 23px; background: var(--gold); border-radius: 4px; color: #1b1c20; font-size: 9.5px; font-weight: 600; line-height: 23px; text-align: center; }
  .nav-icons { position: absolute; left: 0; top: 0; }
  .highlight { position: absolute; left: 900px; top: 5px; width: 33px; height: 36px; border: 2.5px solid var(--alert); }

  .headline { position: absolute; left: 57px; top: 104px; font-size: 45px; font-weight: 700; line-height: 53px; letter-spacing: 0.2px; }
  .headline .accent { color: var(--gold); }

  .market-card { position: absolute; left: 609px; top: 84px; width: 375px; height: 194px; background: var(--card); border-radius: 12px; }
  .coin-row { position: absolute; left: 18px; width: 340px; height: 20px; font-size: 10.5px; }
  .coin-icon { position: absolute; left: 0; top: 1px; width: 18px; height: 18px; border-radius: 50%; }
  .coin-ticker { position: absolute; left: 28px; top: 3px; font-weight: 600; }
  .coin-ticker span { color: var(--muted); font-weight: 400; font-size: 9px; margin-left: 2px; }
  .coin-price { position: absolute; right: 93px; top: 3px; font-weight: 500; }
  .coin-change { position: absolute; right: 0; top: 3px; color: var(--down); font-weight: 500; }
  .view-all { position: absolute; left: 18px; top: 169px; font-size: 8.5px; color: var(--muted); }

  .pointer { position: absolute; left: 0; top: 0; }

  .footer-band { position: absolute; left: 50px; top: 728px; width: 1100px; height: 42px; background: var(--lime); font-weight: 700; font-size: 18.5px; letter-spacing: 0.8px; line-height: 42px; padding-left: 40px; white-space: nowrap; }
</style>
</head>
<body>
<div class="page">
  <div class="frame"></div>

  <h1 class="step-title">STEP 3</h1>
  <div class="section-tag">OPEN <strong>FUTURES ACCOUNT</strong></div>

  <p class="body-text t1">If you have already opened a Futures account, you can skip this step.</p>
  <p class="body-text t2">Once you are connected, move your mouse over the second icon on the top right area of<br>the screen.</p>

  <div class="screen">
    <div class="nav">
      <div class="brand"><span class="brand-mark"></span>KORVANE</div>
      <div class="nav-links">
        <span>Buy Crypto</span><span>Markets</span><span>Trade ˅</span><span>Futures ˅</span><span>Earn</span><span>Plaza ˅</span><span>More ˅</span>
      </div>
      <svg class="nav-icons" width="1029" height="44" viewBox="0 0 1029 44">
        <g fill="none" stroke="#f5f5f5" stroke-width="2">
          <circle cx="774" cy="21" r="5"/><line x1="778" y1="25" x2="781" y2="28"/>
        </g>
        <circle cx="885" cy="22" r="7" fill="#f5f5f5"/>
        <circle cx="885" cy="19.5" r="2.5" fill="#1b1c20"/>
        <rect x="910" y="15" width="13" height="13" rx="2" fill="#f5f5f5"/>
        <rect x="912" y="19" width="9" height="2" fill="#1b1c20"/>
        <path d="M943 27 h12 l-2 -3 v-4 a4 4 0 0 0 -8 0 v4 z" fill="#f5f5f5"/>
        <circle cx="956" cy="14" r="2.5" fill="#f0b90b"/>
        <rect x="972" y="15" width="12" height="13" rx="2" fill="none" stroke="#f5f5f5" stroke-width="2"/>
        <rect x="976" y="20" width="4" height="3" fill="#f5f5f5"/>
        <circle cx="1009" cy="21" r="7" fill="none" stroke="#f5f5f5" stroke-width="2"/>
        <line x1="1002" y1="21" x2="1016" y2="21" stroke="#f5f5f5" stroke-width="1.5"/>
        <ellipse cx="1009" cy="21" rx="3" ry="7" fill="none" stroke="#f5f5f5" stroke-width="1.5"/>
      </svg>
      <div class="deposit">⤓ Deposit</div>
      <div class="highlight"></div>
    </div>

    <svg class="pointer" width="1029" height="290" viewBox="0 0 1029 290">
      <line x1="830" y1="77" x2="888" y2="48" stroke="#e8321f" stroke-width="2.5"/>
      <polygon points="897,43 880,43 887,55" fill="#e8321f"/>
    </svg>

    <h2 class="headline"><span class="accent">Get Verified</span> and<br>Start Your Crypto<br>Journey</h2>

    <div class="market-card">
      <div class="coin-row" style="top:21px"><span class="coin-icon" style="background:#f7931a"></span><span class="coin-ticker">AMB<span>Ambercoin</span></span><span class="coin-price">$51,000.28</span><span class="coin-change">-1.37%</span></div>
      <div class="coin-row" style="top:58px"><span class="coin-icon" style="background:#6f7ce8"></span><span class="coin-ticker">LMN<span>Lumenet</span></span><span class="coin-price">$2,932.03</span><span class="coin-change">-2.13%</span></div>
      <div class="coin-row" style="top:95px"><span class="coin-icon" style="background:#f0b90b"></span><span class="coin-ticker">KVN<span>KVN</span></span><span class="coin-price">$377.80</span><span class="coin-change">-0.50%</span></div>
      <div class="coin-row" style="top:132px"><span class="coin-icon" style="background:#3a3d44"></span><span class="coin-ticker">TDL<span>Tidalcoin</span></span><span class="coin-price">$0.5364</span><span class="coin-change">-1.56%</span></div>
      <div class="view-all">View All 350+ Coins ›</div>
    </div>
  </div>

  <p class="body-text t3">Select “Futures” on the drop-down list that appears.</p>

  <div class="footer-band">BRINDLEQUAY COPY TRADING TUTORIAL</div>
</div>
</body>
</html>
```